Invesment management business need a stationery design

We need a stationery design for a new company based in Sao Paulo, Brazil, called "Brixwell Capital". We provide investment management services for individuals and corporations.
The final design should communicate financial safety and some kind of luxury, just like an investment bank does.
As an inspiration, the designer could take a look at companies like KT Hollins, Fenwick Ardsley, RQT or Talbrook Vesse

Target Market(s)

Individuals and corporations

Industry/Entity Type

Business

Requirements
Must have
• My project must have our logo on it.
• Our business cards should have our contact information, such as telephone number and emails.

```html
<!DOCTYPE html>
<html lang="en">
<head>
<meta charset="utf-8">
<title>Brixwell Capital – Stationery</title>
<link rel="stylesheet" href="https://fonts.googleapis.com/css2?family=Cinzel:wght@400&family=Didact+Gothic&family=Lato:wght@700&display=swap">
<style>
  :root {
    --page-bg-top: #eef1f2;
    --page-bg-bottom: #dfe4e6;
    --panel-dark: #2e2e2e;
    --folder-dark: #2b2b2b;
    --paper: #ffffff;
    --rule-grey: #7a7a7a;
    --muted-grey: #8c8c8c;
    --brand-ink: #c4c4c4;
    --body-ink: #3a3a3a;
    --slogan-ink: #d8d8d8;
    --mark-blue: #3d8fc4;
  }
  * { margin: 0; padding: 0; box-sizing: border-box; }
  html, body { width: 1200px; height: 782px; overflow: hidden; }
  body {
    position: relative;
    background: linear-gradient(180deg, var(--page-bg-top), var(--page-bg-bottom));
    font-family: "Didact Gothic", "Century Gothic", sans-serif;
  }

  .letterhead, .folder {
    position: absolute;
    top: 44px;
    height: 686px;
    border-radius: 14px;
    overflow: hidden;
    box-shadow: 0 3px 10px rgba(0,0,0,0.25);
  }

  /* Brand name block */
  .brand {
    position: absolute; display: flex; align-items: center; gap: 12px;
    font-family: "Didact Gothic", "Century Gothic", sans-serif;
    font-weight: 400; color: var(--brand-ink); white-space: nowrap;
  }
  .brand__dot { border-radius: 50%; background: var(--mark-blue); flex: none; }

  /* Letterhead */
  .letterhead { left: 53px; width: 504px; background: var(--paper); }
  .letterhead__header {
    position: absolute; left: 0; top: 0; width: 100%; height: 108px;
    background: var(--panel-dark);
  }
  .letterhead .brand { left: 16px; top: 17px; }
  .letterhead .brand__dot { width: 46px; height: 46px; }
  .letterhead .brand__name { font-size: 22px; }

  .letterhead__rule {
    position: absolute; left: 83px; top: 69px; width: 414px; height: 3px;
    background: var(--rule-grey);
  }
  .letterhead__web {
    position: absolute; right: 8px; top: 76px;
    font-family: "Lato", sans-serif; font-weight: 700; font-size: 11px;
    color: var(--muted-grey);
  }
  .letterhead__body {
    position: absolute; left: 43px; top: 138px; width: 422px;
    font-size: 11px; line-height: 17.6px; color: var(--body-ink);
    text-align: justify;
  }
  .letterhead__body p { margin-bottom: 17.6px; }
  .signature {
    position: absolute; left: 375px; top: 574px; color: var(--body-ink);
  }
  .signature__name { font-size: 14px; }
  .signature__title { font-size: 9px; margin-top: 6px; }
  .letterhead__footer {
    position: absolute; left: 0; bottom: 0; width: 100%; height: 40px;
    background: var(--panel-dark);
    display: flex; align-items: center; justify-content: center;
    font-family: "Cinzel", serif; font-size: 13px; letter-spacing: 1px;
    color: var(--slogan-ink);
  }

  /* Folder */
  .folder { left: 636px; width: 505px; background: var(--folder-dark); }
  .folder__slit { position: absolute; right: 0; top: 116px; }
  .folder .brand { left: 118px; top: 576px; gap: 14px; }
  .folder .brand__dot { width: 66px; height: 66px; }
  .folder .brand__name { font-size: 28px; }
</style>
</head>
<body>

<section class="letterhead">
  <header class="letterhead__header">
    <div class="brand">
      <span class="brand__dot"></span>
      <span class="brand__name">Brixwell Capital</span>
    </div>
    <div class="letterhead__rule"></div>
    <div class="letterhead__web">www.brixwell.com.br</div>
  </header>

  <div class="letterhead__body">
    <p>Lorem ipsum dolor sit amet, consectetur adipiscing elit. Donec orci purus, luctus vitae dignissim eu, iaculis sed purus. Vivamus faucibus, ipsum nec aliquet viverra, leo mauris condimentum ligula, sit amet sagittis enim ligula quis arcu. Nam egestas tortor id nisi porttitor mattis. In tortor ante, ultricies in suscipit a, tempus non massa. Vivamus et auctor mi. Fusce vel massa nulla. Phasellus nec eros mauris, et scelerisque orci. Donec malesuada orci vitae nulla accumsan porta a id massa.</p>
    <p>Quisque accumsan iaculis magna sit amet fringilla. Maecenas consequat, magna eget tincidunt semper, odio nibh rutrum mi, id feugiat ante nisi eu risus. Vestibulum nunc orci, rhoncus a placerat in, ultricies in mi. Cras mattis varius eros, vel fringilla nisi suscipit eget. Quisque scelerisque sagittis nulla at porttitor. Mauris a justo et tellus interdum tristique. Sed id augue vitae urna euismod commodo aliquet a quam. Pellentesque arcu velit, cursus et malesuada ut, consequat et diam. Nullam erat sem, rhoncus id ullamcorper vitae, rhoncus et arcu. In ultricies ultricies nulla,</p>
    <p>Kut rutrum nisi iaculis at. Donec eu magna a metus ornare faucibus. Fusce aliquet faucibus ultricies. Morbi semper, est id tincidunt gravida, sem arcu adipiscing lacus, ac bibendum nulla leo eu purus. Quisque nec diam sed risus consectetur a ccumsan quis quis nibh. Vestibulum id purus lorem. Donec eu magna a metus ornare faucibus. Fusce aliquet faucibus ultricies. Morbi semper, est id tincidunt gravida, sem arcu adipiscing lacus, ac bibendum nulla leo eu purus. Quisque nec diam sed risus consectetur a ccumsan quis quis nibh. Vestibulum id purus lorem.</p>
  </div>

  <div class="signature">
    <div class="signature__name">Rafael Duarte</div>
    <div class="signature__title">Co-Founder &amp; CEO</div>
  </div>

  <footer class="letterhead__footer">YOUR SLOGAN / TAG LINE HERE</footer>
</section>

<section class="folder">
  <svg class="folder__slit" width="14" height="250" viewBox="0 0 14 250" aria-hidden="true">
    <path d="M14 0 V10 Q14 38 4 44 V250 H14 Z" fill="#242424"/>
    <path d="M14 10 Q14 38 4 44 V250" fill="none" stroke="#1c1c1c" stroke-width="1"/>
  </svg>
  <div class="brand">
    <span class="brand__dot"></span>
    <span class="brand__name">Brixwell Capital</span>
  </div>
</section>

</body>
</html>
```